Business Development website and logo (www.kwalrun.eu)

Based on an existing website structure (http://tamford.velunquo.com) fully redesign the site including: colors, images, technology and logo. Kwalrun is intended to provide Europe and LATAM Business Development services. The site and logo should communicate modern, professional and experienced sales services.

Target Market(s)

Tech companies wanting to expand into new territories

Industry/Entity Type

Tech

Logo Text

It has to be an abstract design, no letters

Coding

Coded - Design and coding required

Number of Pages Required

5+ page

Font styles to use
Sans Serif

Colors

Designer to choose colors to be used in the design.

Requirements
Must have
• - The site and logo should communicate modern, professional and experienced sales services.
• - All the pages included in the example site: http://tamford.velunquo.com (Company, Careers, Bs Dev, Sales, etc..)
Nice to have
• - Sober design
Should not have
• - Fun design as this one: http://velunquo.com/

```html
<!DOCTYPE html>
<html lang="en">
<head>
<meta charset="utf-8">
<title>Kwalrun – Business Development</title>
<link href="https://fonts.googleapis.com/css2?family=Roboto:wght@400;500;700;900&family=Roboto+Condensed:wght@700&display=swap" rel="stylesheet">
<style>
:root{
  --blue:#1a8fd8;
  --blue-dark:#1479bd;
  --footer:#1f8bd3;
  --ink:#222831;
  --text:#6b7280;
  --light:#f1f4f7;
  --white:#ffffff;
  --hero-a:#2c3440;
  --hero-b:#5b4f47;
}
*{box-sizing:border-box;margin:0;padding:0}
html,body{width:776px;height:1200px;overflow:hidden;background:var(--white)}
body{font-family:"Roboto",Arial,sans-serif;color:var(--ink);position:relative}
a{text-decoration:none;color:inherit}

.hero{position:absolute;left:0;top:0;width:776px;height:390px;background:linear-gradient(120deg,var(--hero-a),var(--hero-b) 55%,#3b4a5a);}
.hero-photo{position:absolute;inset:0;background:radial-gradient(ellipse at 60% 35%,rgba(200,170,140,.35),transparent 60%),linear-gradient(180deg,rgba(0,0,0,.05),rgba(0,0,0,.45))}
.slider-dots{position:absolute;left:44px;top:172px;display:flex;flex-direction:column;gap:10px}
.slider-dots span{width:7px;height:7px;border-radius:50%;background:rgba(255,255,255,.5)}
.slider-dots span.active{background:var(--white)}
.brand{position:absolute;top:96px;left:0;width:100%;display:flex;justify-content:center;align-items:center;gap:10px}
.brand-mark{width:30px;height:30px;background:var(--blue)}
.brand-name{color:var(--white);font-weight:700;font-size:24px}
.hero-title{position:absolute;top:176px;width:100%;text-align:center;color:var(--white);font-family:"Roboto Condensed",Arial,sans-serif;font-weight:700;font-size:30px;letter-spacing:.5px}
.hero-sub{position:absolute;top:214px;left:238px;width:300px;text-align:center;color:rgba(255,255,255,.85);font-size:8.5px;line-height:13px}
.btn{position:absolute;top:250px;left:314px;width:148px;height:32px;background:var(--blue);color:var(--white);font-size:11px;font-weight:500;display:flex;align-items:center;justify-content:center;border-radius:2px}

.nav-band{position:absolute;top:390px;left:0;width:776px;height:34px;background:var(--white);border-top:6px solid var(--blue)}
.nav{display:flex;justify-content:center;height:28px;align-items:center;gap:6px}
.nav a{font-size:9.5px;padding:6px 10px;color:var(--ink)}
.nav a.active{background:var(--blue);color:var(--white)}

.welcome{position:absolute;top:455px;width:100%;text-align:center}
.welcome h2{font-size:24px;font-weight:700}
.welcome h2 span{color:var(--blue)}
.welcome p{margin:12px auto 0;width:470px;font-size:8.5px;line-height:13px;color:var(--text)}

.services{position:absolute;top:574px;left:103px;width:570px;display:flex;gap:10px}
.card{flex:1;background:var(--white);box-shadow:0 1px 4px rgba(0,0,0,.15);height:166px}
.card-img{height:84px}
.card h3{font-size:9.5px;font-weight:700;margin:9px 8px 4px}
.card p{font-size:7.5px;line-height:11px;color:var(--text);margin:0 8px}
.read{display:block;font-size:7.5px;color:var(--blue);margin:6px 8px 0;font-weight:500}

.call{position:absolute;top:789px;left:103px;width:570px;height:78px;display:flex;background:var(--light)}
.call-left{width:210px;background:var(--blue);color:var(--white);display:flex;align-items:center;gap:10px;padding-left:18px;clip-path:polygon(0 0,100% 0,88% 100%,0 100%)}
.call-left small{font-size:9px}
.icon-ring{width:28px;height:28px;border:1.5px solid var(--white);border-radius:50%;display:flex;align-items:center;justify-content:center}
.call-left strong{font-size:14px;font-weight:700}
.call-right{flex:1;padding:12px 18px}
.call-right p{font-size:7.5px;line-height:11px;color:var(--text)}
.mail{display:flex;align-items:center;gap:10px;margin-top:8px;font-size:9px}
.mail b{color:var(--blue);font-size:12px;font-weight:500}

.news-title{position:absolute;top:888px;width:100%;text-align:center;font-size:24px;font-weight:700}
.news-title span{color:var(--blue)}
.news{position:absolute;top:936px;left:135px;width:512px;display:flex;gap:14px}
.post{flex:1;display:flex;gap:8px;box-shadow:0 1px 4px rgba(0,0,0,.15);height:98px;padding:6px}
.post-img{width:100px;flex:none}
.post small{font-size:6.5px;color:var(--blue)}
.post h4{font-size:8.5px;margin:2px 0 3px}
.post p{font-size:6.8px;line-height:10px;color:var(--text)}

.footer{position:absolute;top:1080px;left:0;width:776px;height:120px;background:var(--footer);color:var(--white)}
.footer-nav{display:flex;justify-content:center;gap:28px;font-size:9px;padding-top:18px}
.footer hr{border:0;border-top:1px solid rgba(255,255,255,.35);margin:18px 100px 0}
.footer-info{display:flex;justify-content:center;gap:36px;align-items:center;margin-top:18px;font-size:7.5px}
.footer-info div{display:flex;align-items:center;gap:8px}
.dot-icon{width:22px;height:22px;border:1px solid var(--white);border-radius:50%;display:flex;align-items:center;justify-content:center}
</style>
</head>
<body>

<header class="hero">
  <div class="hero-photo" role="img" aria-label="Photo of a business team working together around a laptop"></div>
  <div class="slider-dots"><span class="active"></span><span></span><span></span></div>
  <div class="brand"><span class="brand-mark"></span><span class="brand-name">Kwalrun</span></div>
  <h1 class="hero-title">BUSINESS DEVLOPMENT</h1>
  <p class="hero-sub">Lorem ipsum is simply dummy text of the printing and typesetting industry. Lorem ipsum has been the standard dummy text ever since the 1500s.</p>
  <a class="btn" href="#">Get A Free Consulting</a>
</header>

<nav class="nav-band">
  <div class="nav">
    <a href="#">Home</a><a href="#">About Us</a><a class="active" href="#">Services</a><a href="#">Bs Dev</a><a href="#">Sales</a><a href="#">News</a><a href="#">Contact Us</a>
  </div>
</nav>

<section class="welcome">
  <h2>Welcome To <span>Kwalrun</span></h2>
  <p>Lorem ipsum is simply dummy text of the printing and typesetting industry. Lorem ipsum has been the industry standard dummy text ever since the 1500s, when an unknown printer took a galley of type and scrambled it to make a type specimen book. It has survived not only five centuries but also the leap into electronic typesetting, remaining essentially unchanged.</p>
</section>

<section class="services">
  <article class="card">
    <div class="card-img" role="img" aria-label="Photo of a business development meeting" style="background:linear-gradient(135deg,#8a7a6a,#c9b8a2)"></div>
    <h3>Business Development</h3>
    <p>Lorem ipsum is simply dummy text of the printing and typesetting industry.</p>
    <a class="read" href="#">Read More »</a>
  </article>
  <article class="card">
    <div class="card-img" role="img" aria-label="Photo of a team planning a project at a table" style="background:linear-gradient(135deg,#6f6a66,#b7a999)"></div>
    <h3>Project Deployment</h3>
    <p>Lorem ipsum is simply dummy text of the printing and typesetting industry.</p>
    <a class="read" href="#">Read More »</a>
  </article>
  <article class="card">
    <div class="card-img" role="img" aria-label="Photo of colleagues reviewing documents" style="background:linear-gradient(135deg,#9c8f80,#d8cbbb)"></div>
    <h3>Quality Process</h3>
    <p>Lorem ipsum is simply dummy text of the printing and typesetting industry.</p>
    <a class="read" href="#">Read More »</a>
  </article>
  <article class="card">
    <div class="card-img" role="img" aria-label="Photo of a customer support agent with headset" style="background:linear-gradient(135deg,#5d6670,#a8b2bb)"></div>
    <h3>Customer Support</h3>
    <p>Lorem ipsum is simply dummy text of the printing and typesetting industry.</p>
    <a class="read" href="#">Read More »</a>
  </article>
</section>

<section class="call">
  <div class="call-left">
    <small>Call Us On</small>
    <span class="icon-ring"><svg width="14" height="14" viewBox="0 0 24 24" fill="#fff"><path d="M6.6 10.8a15 15 0 0 0 6.6 6.6l2.2-2.2a1 1 0 0 1 1-.25 11.4 11.4 0 0 0 3.6.57 1 1 0 0 1 1 1V20a1 1 0 0 1-1 1A17 17 0 0 1 3 4a1 1 0 0 1 1-1h3.5a1 1 0 0 1 1 1c0 1.25.2 2.45.57 3.57a1 1 0 0 1-.25 1z"/></svg></span>
    <strong>+91-000-000-0000</strong>
  </div>
  <div class="call-right">
    <p>Lorem ipsum is simply dummy text of the printing and typesetting industry. Lorem ipsum has been the standard dummy text ever since the 1500s.</p>
    <div class="mail">
      <span>Mail Us On</span>
      <span class="icon-ring" style="border-color:var(--blue)"><svg width="13" height="13" viewBox="0 0 24 24" fill="none" stroke="#1a8fd8" stroke-width="2"><rect x="3" y="5" width="18" height="14"/><path d="M3 6l9 7 9-7"/></svg></span>
      <b>info@kwalrun.eu</b>
    </div>
  </div>
</section>

<h2 class="news-title">Latest <span>News</span></h2>
<section class="news">
  <article class="post">
    <div class="post-img" role="img" aria-label="Photo of a team meeting in an office" style="background:linear-gradient(135deg,#7d7367,#c2b4a2)"></div>
    <div>
      <small>12 March 2024</small>
      <h4>Lorem Ipsum is simply dummy text</h4>
      <p>Lorem ipsum is simply dummy text of the printing and typesetting industry. Lorem ipsum has been the standard.</p>
      <a class="read" href="#" style="margin:4px 0 0">Read More »</a>
    </div>
  </article>
  <article class="post">
    <div class="post-img" role="img" aria-label="Photo of a conference room presentation" style="background:linear-gradient(135deg,#6e7a84,#b9c3c9)"></div>
    <div>
      <small>18 March 2024</small>
      <h4>Lorem Ipsum is simply dummy text</h4>
      <p>Lorem ipsum is simply dummy text of the printing and typesetting industry. Lorem ipsum has been the standard.</p>
      <a class="read" href="#" style="margin:4px 0 0">Read More »</a>
    </div>
  </article>
</section>

<footer class="footer">
  <div class="footer-nav"><a href="#">Home</a><a href="#">About Us</a><a href="#">Services</a><a href="#">Bs Dev</a><a href="#">Sales</a><a href="#">News</a><a href="#">Contact Us</a></div>
  <hr>
  <div class="footer-info">
    <div><span class="dot-icon"><svg width="11" height="11" viewBox="0 0 24 24" fill="#fff"><path d="M6.6 10.8a15 15 0 0 0 6.6 6.6l2.2-2.2a1 1 0 0 1 1-.25 11.4 11.4 0 0 0 3.6.57 1 1 0 0 1 1 1V20a1 1 0 0 1-1 1A17 17 0 0 1 3 4a1 1 0 0 1 1-1h3.5a1 1 0 0 1 1 1c0 1.25.2 2.45.57 3.57a1 1 0 0 1-.25 1z"/></svg></span>+91-000-000-0000</div>
    <div><span class="dot-icon"><svg width="11" height="11" viewBox="0 0 24 24" fill="none" stroke="#fff" stroke-width="2"><rect x="3" y="5" width="18" height="14"/><path d="M3 6l9 7 9-7"/></svg></span>info@kwalrun.eu</div>
    <div><span class="dot-icon"><svg width="11" height="11" viewBox="0 0 24 24" fill="#fff"><path d="M12 2a7 7 0 0 0-7 7c0 5 7 13 7 13s7-8 7-13a7 7 0 0 0-7-7zm0 9.5A2.5 2.5 0 1 1 12 6.5a2.5 2.5 0 0 1 0 5z"/></svg></span>123, Lorem Ipsum Street, Dolor City</div>
    <div>Copyright © 2024 Kwalrun. All Rights Reserved.</div>
  </div>
</footer>

</body>
</html>
```